Antibacterial Hand Wash Squeeze Tube Label

We're looking for a contemporary label design for a new Antibacterial Hand Wash for an 8oz squeeze tube. The new consumer brand will be sold to consumers in major US retail stores & online. The moisturizing hand wash contains Aloe Vera, vitamin E, and other natural ingredients so the design should include the color green. Real photos are very effective on packaging, so a picture of Aloe Vera or possibly two hands washing would help draw consumers' attention to the tube on the retail shelf. The front label may wrap around the sides. Rear must be left mostly blank
US Consumers - retail stores & online
Consumer

```html
<!DOCTYPE html>
<html lang="en">
<head>
<meta charset="utf-8">
<title>Antibacterial Hand Wash – Tube Label</title>
<link href="https://fonts.googleapis.com/css2?family=Arimo:wght@400;700&display=swap" rel="stylesheet">
<style>
  :root {
    --page-bg: #eef0ec;
    --green-light: #a9cf4e;
    --green-mid: #74ad2c;
    --green-deep: #4f8a1c;
    --rule: #d5ea7a;
    --ink: #f4f9e6;
    --ink-soft: rgba(244, 249, 230, 0.85);
    --pill-bg: #5a9222;
  }
  * { box-sizing: border-box; margin: 0; padding: 0; }
  html, body { width: 1200px; height: 1000px; overflow: hidden; }
  body {
    background: var(--page-bg);
    font-family: "Arimo", Arial, sans-serif;
    color: var(--ink);
    display: flex;
    align-items: center;
    justify-content: center;
    gap: 80px;
  }
  .label {
    position: relative;
    width: 380px;
    height: 820px;
    border-radius: 6px;
    background:
      radial-gradient(circle at 30% 35%, rgba(255,255,255,0.10) 0 40px, transparent 41px),
      radial-gradient(circle at 75% 60%, rgba(255,255,255,0.08) 0 55px, transparent 56px),
      radial-gradient(circle at 20% 78%, rgba(255,255,255,0.07) 0 35px, transparent 36px),
      linear-gradient(160deg, var(--green-light) 0%, var(--green-mid) 45%, var(--green-deep) 100%);
    display: flex;
    flex-direction: column;
    align-items: center;
    overflow: hidden;
  }
  .rule { width: 100%; height: 2px; background: var(--rule); }
  .icon-row { display: flex; gap: 60px; justify-content: center; }
  .icon { width: 56px; height: 56px; }
  .icon-art {
    width: 56px; height: 56px; border-radius: 50%;
    background: radial-gradient(circle, rgba(255,255,255,0.85), rgba(255,255,255,0.35));
  }
  .title { font-weight: 400; font-size: 40px; line-height: 1; letter-spacing: 0.2px; }
  .subtitle { font-size: 20px; letter-spacing: 1px; color: var(--ink-soft); }
  .pill {
    border: 1.5px solid var(--rule);
    background: var(--pill-bg);
    border-radius: 20px;
    padding: 5px 18px;
    font-size: 15px;
    font-weight: 700;
  }
  /* back panel */
  .back .icons { margin-top: 60px; display: flex; flex-direction: column; align-items: center; gap: 18px; }
  .back .rule { margin-top: 30px; }
  .benefit-list { margin-top: 40px; list-style: none; font-size: 17px; line-height: 1.9; align-self: flex-start; margin-left: 110px; }
  .benefit-list li::before { content: "•"; margin-right: 10px; }
  .back .brand-block { margin-top: 40px; text-align: center; }
  .back .title { font-size: 30px; }
  .back .subtitle { font-size: 16px; }
  .back .pill { margin-top: 24px; }
  /* front panel */
  .front .rule.top { margin-top: 90px; }
  .front .brand-block { margin: 26px 0; text-align: center; }
  .front .title { font-size: 46px; }
  .front .subtitle { margin-top: 6px; }
  .feature-list { margin-top: 40px; display: flex; flex-direction: column; align-items: center; gap: 14px; }
  .feature { display: flex; flex-direction: column; align-items: center; gap: 6px; font-size: 15px; }
  .front .pill { margin-top: 40px; }
</style>
</head>
<body>

<!-- Back label -->
<section class="label back">
  <div class="icons">
    <svg class="icon" viewBox="0 0 56 56" aria-label="Anti bacterial icon">
      <circle cx="28" cy="28" r="24" fill="none" stroke="#fff" stroke-width="4"/>
      <circle cx="28" cy="28" r="9" fill="#fff"/>
      <line x1="11" y1="45" x2="45" y2="11" stroke="#fff" stroke-width="4"/>
    </svg>
    <div class="icon-row">
      <div class="icon-art" role="img" aria-label="Aloe vera leaves icon"></div>
      <div class="icon-art" role="img" aria-label="Caring hands icon"></div>
    </div>
    <svg class="icon" viewBox="0 0 56 56" aria-label="Vitamin E drop">
      <path d="M28 4 C38 20 46 30 46 38 A18 18 0 0 1 10 38 C10 30 18 20 28 4Z" fill="#fff"/>
      <text x="28" y="44" text-anchor="middle" font-family="Arimo, sans-serif" font-size="16" font-weight="700" fill="#6aa328">E</text>
    </svg>
  </div>
  <div class="rule"></div>
  <ul class="benefit-list">
    <li>Anti Bacterial</li>
    <li>Moisturizing</li>
    <li>Anti Bacterial</li>
    <li>Vitamin E</li>
    <li>Other Natural Ingredient</li>
  </ul>
  <div class="brand-block">
    <h2 class="title">Antibacterial</h2>
    <p class="subtitle">HAND WASH</p>
  </div>
  <div class="pill">8Oz (240ml)</div>
</section>

<!-- Front label -->
<section class="label front">
  <div class="rule top"></div>
  <div class="brand-block">
    <h1 class="title">Antibacterial</h1>
    <p class="subtitle">HAND WASH</p>
  </div>
  <div class="rule"></div>
  <div class="feature-list">
    <div class="feature">
      <svg class="icon" viewBox="0 0 56 56" aria-label="Anti bacterial icon">
        <circle cx="28" cy="28" r="24" fill="none" stroke="#fff" stroke-width="4"/>
        <circle cx="28" cy="28" r="9" fill="#fff"/>
        <line x1="11" y1="45" x2="45" y2="11" stroke="#fff" stroke-width="4"/>
      </svg>
      <span>Anti Bacterial</span>
    </div>
    <div class="feature">
      <div class="icon-art" role="img" aria-label="Caring hands icon"></div>
      <span>Moisturizing</span>
    </div>
    <div class="feature">
      <div class="icon-art" role="img" aria-label="Aloe vera leaves icon"></div>
      <span>Anti Bacterial</span>
    </div>
    <div class="feature">
      <svg class="icon" viewBox="0 0 56 56" aria-label="Vitamin E drop">
        <path d="M28 4 C38 20 46 30 46 38 A18 18 0 0 1 10 38 C10 30 18 20 28 4Z" fill="#fff"/>
        <text x="28" y="44" text-anchor="middle" font-family="Arimo, sans-serif" font-size="16" font-weight="700" fill="#6aa328">E</text>
      </svg>
      <span>Vitamin E</span>
    </div>
  </div>
  <div class="pill">8Oz (240ml)</div>
</section>

</body>
</html>
```